Birch & Ember Website Design (Rustic/Western)

OVERVIEW
Birch & Ember Supply House (aka Birch & Ember) manufactures rustic / western furniture and décor for cabins, lodges, and ranches. We also offer a line of accessories to complement our product line.
WEB PAGE (www.BirchAndEmber.example)
We are looking for a new web page design to represent our mountain-style (log furniture) and country-style (barnwood furniture) product line. We would like to re-create our existing homepage with a similar style template for our product line.
Our website is currently under construction – a draft has been published as an example outline. We are currently using Plinkora.example for our online store.
THEME
The overall theme needs to appear rustic, yet elegant. Listed below are only suggestions, not requirements. Please use your own creativity.
* Photographs: We will use our own photographs, for now any photograph will suffice.
* Background Colors: dark brown (rgb 21-9-2), medium brown (rgb 39-17-4), light brown (rgb 72-34-3). White background is also an option.
* Font Colors: beige (rgb 233-164-118), gold (rgb 151-98-2)
• Mountain-Style Images: cabin, wildlife, mountains, fishing, wildlife, trees, etc.
* Mountain-Style Colors: hunter green
* Country-Style Images: western, ranch, barn, farm animals, horse buggies, horseshoes, etc.
* Country-Style Colors: maroon
Thanks to all who are participating.
Target Market(s)
Outdoor enthusiasts who enjoy mountain living or country living. Our primary target market is our local market and within a 100 mile radius of our location.
Industry/Entity Type
Construction
Requirements
Must have
- Rustic, yet elegant design.
Homepage and product template page for displaying each item.
Nice to have
- Source code and functionality is optional.
Mountain-Style theme to represent our collection of log furniture and décor suited for cabins and lodges. Suggested color: hunter green. Images may include cabin, wildlife, mountains, fishing, wildlife, trees, etc.
Country-Style theme to represent our collection of barnwood furniture and décor suited for farms and ranches. Suggested color: maroon. Images may include western, ranch, barn, farm animals, horse buggies, horseshoes, etc.

```html
<!DOCTYPE html>
<html lang="en">
<head>
<meta charset="utf-8">
<title>Birch &amp; Ember</title>
<link href="https://fonts.googleapis.com/css2?family=Open+Sans:wght@300;400;600;700&display=swap" rel="stylesheet">
<style>
:root{
  --page:#3e1e08;
  --bar:#1a0b03;
  --search:#120700;
  --panel:#2b2b2b;
  --field:#1c1c1c;
  --white:#ffffff;
  --row:#f4f4f4;
  --row-alt:#ebebeb;
  --ink:#333333;
  --muted:#999999;
  --line:#dddddd;
  --price:#d0361c;
  --dash:#8a6a52;
  --beige:#e9a476;
}
*{margin:0;padding:0;box-sizing:border-box}
html,body{width:1200px;height:2162px;overflow:hidden}
body{position:relative;background:var(--page);font-family:"Open Sans",Arial,sans-serif;color:var(--ink)}
.abs{position:absolute}

.hero{left:0;top:0;width:1200px;height:861px;background:linear-gradient(180deg,#8fb2d4 0%,#c3d6e6 14%,#6f8d74 32%,#47663e 48%,#6f7a4a 62%,#b8a27c 80%,#9c8462 100%)}
.topbar{left:40px;top:36px;width:1120px;height:94px;background:var(--bar);border-radius:5px;box-shadow:0 2px 6px rgba(0,0,0,.5)}
.brand{left:48px;top:35px;color:var(--beige);font-weight:700;font-size:17px;letter-spacing:1px;display:flex;align-items:center;gap:10px;line-height:24px}
.brand i{display:block;width:20px;height:20px;background:var(--beige);border-radius:50%}
.nav{left:510px;top:36px;display:flex;gap:50px;color:var(--white);font-weight:600;font-size:14px;line-height:22px}
.search{left:908px;top:32px;width:186px;height:28px;background:var(--search);border-radius:3px;color:#5a4a3e;font-size:12px;line-height:28px;padding:0 10px}
.search svg{position:absolute;right:9px;top:7px}

.hero-title{left:0;top:292px;width:1200px;text-align:center;color:var(--white);font-weight:300;font-size:45px;line-height:60px;text-shadow:0 1px 4px rgba(0,0,0,.4)}
.hero-sub{left:0;top:374px;width:1200px;text-align:center;color:var(--white);font-weight:300;font-size:20px;line-height:28px;text-shadow:0 1px 3px rgba(0,0,0,.5)}
.arrow{top:333px;width:34px;height:34px;border-radius:50%;background:#1a1a1a}
.arrow svg{display:block;margin:10px auto}

.card{top:562px;width:548px;height:324px;background:var(--white);border-radius:4px;box-shadow:0 2px 6px rgba(0,0,0,.35);overflow:hidden}
.card-photo{height:236px}
.card-title{height:52px;display:flex;justify-content:space-between;align-items:center;padding:0 12px;font-size:12px;font-weight:600;color:#444;border-bottom:1px solid var(--line)}
.stars{display:flex;gap:2px}
.card-meta{display:flex;height:36px;font-size:12px;color:#666}
.card-meta span{display:flex;align-items:center;padding-left:12px}
.card-meta .place{width:195px;border-right:1px solid var(--line)}
.card-meta .cost{flex:1;justify-content:center;padding-left:0}
.price{color:var(--price);font-weight:700}

.dashes{left:40px;width:1120px;border-top:2px dashed var(--dash)}

.finder{left:40px;top:984px;width:1120px;height:386px;box-shadow:0 2px 6px rgba(0,0,0,.4)}
.form{left:0;top:0;width:371px;height:386px;background:var(--panel);border-radius:4px 0 0 4px}
.tabs{left:22px;top:17px;display:flex;gap:28px;color:var(--white);font-weight:600;font-size:14px;line-height:20px}
.tab-notch{left:44px;top:48px;width:0;height:0;border:7px solid transparent;border-bottom-color:#3a3a3a}
.tab-rule{left:0;top:54px;width:371px;border-top:1px solid #3a3a3a}
.lbl{text-transform:uppercase;letter-spacing:.5px;font-size:10px;color:#9a9a9a}
.field{height:31px;background:var(--field);border:1px solid #111;border-radius:2px;color:#aaa;font-size:12px;line-height:29px;padding:0 8px}
.btn{left:23px;top:331px;width:323px;height:33px;border-radius:3px;background:linear-gradient(#5a5a5a,#3d3d3d);color:var(--white);text-align:center;font-size:12px;font-weight:600;line-height:33px}

.table{left:371px;top:0;width:749px;height:386px;background:var(--white);border-radius:0 4px 4px 0;overflow:hidden}
.trow{display:flex;height:47.4px;align-items:center;font-size:12px;border-bottom:1px solid var(--line)}
.trow:nth-child(odd){background:var(--row-alt)}
.trow:nth-child(even){background:var(--row)}
.trow.head{height:54px;background:var(--white);font-size:10px;color:var(--muted);letter-spacing:.5px}
.c1{width:152px;padding-left:21px;font-weight:600}
.head .c1{font-weight:400}
.c2{width:182px}.c3{width:155px}.c4{width:110px}.c5{flex:1}
.old{color:#888;text-decoration:line-through;margin-right:10px}

.post{top:1468px;width:356px;height:514px;background:var(--white);border-radius:3px;box-shadow:0 2px 6px rgba(0,0,0,.35);overflow:hidden}
.post-photo{height:234px}
.post-title{font-size:20px;font-weight:400;color:#444;line-height:28px;padding:22px 22px 6px}
.post-meta{display:flex;font-size:11px;color:var(--muted);line-height:16px;padding:0 22px 10px;margin:0 0 14px}
.post-meta span{padding-right:14px;margin-right:14px;border-right:1px solid #ddd}
.post-meta span:last-child{border:0}
.post-meta b{color:#555;font-weight:600}
.post-body{font-size:12.5px;line-height:27px;color:#555;padding:0 22px;text-align:justify}

.footer-rule{left:0;top:2030px;width:1200px;border-top:1px solid #7a5a42}
.foot-nav{left:40px;top:2070px;display:flex;gap:34px;color:var(--white);font-size:12px;font-weight:600;line-height:18px}
.copy{left:40px;top:2106px;color:#e0d4c8;font-size:12px;line-height:18px}
.contact{right:40px;top:2063px;text-align:right;color:var(--white);font-size:12px;line-height:23px;font-style:normal}
</style>
</head>
<body>

<div class="abs hero" role="img" aria-label="Mountain valley with terraced stone ruins under a blue sky"></div>

<header class="abs topbar">
  <div class="abs brand"><i></i>Birch &amp; Ember</div>
  <nav class="abs nav"><span>Browse</span><span>Pages</span><span>Blog</span><span>Contact</span></nav>
  <div class="abs search">Search...
    <svg width="14" height="14" viewBox="0 0 16 16"><circle cx="6.5" cy="6.5" r="4.5" fill="none" stroke="#777" stroke-width="2"/><line x1="10" y1="10" x2="14" y2="14" stroke="#777" stroke-width="2.5"/></svg>
  </div>
</header>

<h1 class="abs hero-title">The Lodgepole Collection from 799 €</h1>
<p class="abs hero-sub">Log beds, tables, benches, lamps and mirrors</p>
<div class="abs arrow" style="left:39px"><svg width="14" height="14" viewBox="0 0 14 14"><path d="M9 2 L4 7 L9 12" fill="none" stroke="#fff" stroke-width="2.5"/></svg></div>
<div class="abs arrow" style="left:1125px"><svg width="14" height="14" viewBox="0 0 14 14"><path d="M5 2 L10 7 L5 12" fill="none" stroke="#fff" stroke-width="2.5"/></svg></div>

<article class="abs card" style="left:40px">
  <div class="card-photo" role="img" aria-label="Orange autumn trees below a mountain range" style="background:linear-gradient(180deg,#7d9fc7 0%,#a9bfd8 35%,#7a7f80 52%,#d4561a 70%,#b9451a 85%,#8a6f4b 100%)"></div>
  <div class="card-title">MOUNTAIN-STYLE COLLECTION
    <div class="stars">
      <svg width="12" height="12" viewBox="0 0 10 10"><path d="M5 .5l1.3 2.9 3.2.3-2.4 2.1.7 3.1L5 7.3 2.2 8.9l.7-3.1L.5 3.7l3.2-.3z" fill="#bbb"/></svg>
      <svg width="12" height="12" viewBox="0 0 10 10"><path d="M5 .5l1.3 2.9 3.2.3-2.4 2.1.7 3.1L5 7.3 2.2 8.9l.7-3.1L.5 3.7l3.2-.3z" fill="#bbb"/></svg>
      <svg width="12" height="12" viewBox="0 0 10 10"><path d="M5 .5l1.3 2.9 3.2.3-2.4 2.1.7 3.1L5 7.3 2.2 8.9l.7-3.1L.5 3.7l3.2-.3z" fill="#bbb"/></svg>
      <svg width="12" height="12" viewBox="0 0 10 10"><path d="M5 .5l1.3 2.9 3.2.3-2.4 2.1.7 3.1L5 7.3 2.2 8.9l.7-3.1L.5 3.7l3.2-.3z" fill="none" stroke="#ccc"/></svg>
      <svg width="12" height="12" viewBox="0 0 10 10"><path d="M5 .5l1.3 2.9 3.2.3-2.4 2.1.7 3.1L5 7.3 2.2 8.9l.7-3.1L.5 3.7l3.2-.3z" fill="none" stroke="#ccc"/></svg>
    </div>
  </div>
  <div class="card-meta"><span class="place">Log furniture</span><span class="cost"><b class="price">1 899 €</b>&nbsp;/ 10 pieces</span></div>
</article>

<article class="abs card" style="left:613px">
  <div class="card-photo" role="img" aria-label="Herd of cattle in front of a farmhouse and barn" style="background:linear-gradient(180deg,#3f6fb8 0%,#7aa0d2 30%,#8e8b78 48%,#3e5a2a 62%,#c9bfae 78%,#4d5b30 100%)"></div>
  <div class="card-title">COUNTRY-STYLE COLLECTION
    <div class="stars">
      <svg width="12" height="12" viewBox="0 0 10 10"><path d="M5 .5l1.3 2.9 3.2.3-2.4 2.1.7 3.1L5 7.3 2.2 8.9l.7-3.1L.5 3.7l3.2-.3z" fill="#bbb"/></svg>
      <svg width="12" height="12" viewBox="0 0 10 10"><path d="M5 .5l1.3 2.9 3.2.3-2.4 2.1.7 3.1L5 7.3 2.2 8.9l.7-3.1L.5 3.7l3.2-.3z" fill="#bbb"/></svg>
      <svg width="12" height="12" viewBox="0 0 10 10"><path d="M5 .5l1.3 2.9 3.2.3-2.4 2.1.7 3.1L5 7.3 2.2 8.9l.7-3.1L.5 3.7l3.2-.3z" fill="#bbb"/></svg>
      <svg width="12" height="12" viewBox="0 0 10 10"><path d="M5 .5l1.3 2.9 3.2.3-2.4 2.1.7 3.1L5 7.3 2.2 8.9l.7-3.1L.5 3.7l3.2-.3z" fill="none" stroke="#ccc"/></svg>
      <svg width="12" height="12" viewBox="0 0 10 10"><path d="M5 .5l1.3 2.9 3.2.3-2.4 2.1.7 3.1L5 7.3 2.2 8.9l.7-3.1L.5 3.7l3.2-.3z" fill="none" stroke="#ccc"/></svg>
    </div>
  </div>
  <div class="card-meta"><span class="place">Barnwood furniture</span><span class="cost"><b class="price">1 899 €</b>&nbsp;/ 10 pieces</span></div>
</article>

<div class="abs dashes" style="top:934px"></div>

<section class="abs finder">
  <div class="abs form">
    <div class="abs tabs"><span>Find a piece</span><span>Find a style</span><span>Orders</span></div>
    <div class="abs tab-notch"></div>
    <div class="abs tab-rule"></div>
    <div class="abs lbl" style="left:23px;top:83px">Collection</div>
    <div class="abs field" style="left:23px;top:106px;width:323px">All</div>
    <div class="abs lbl" style="left:23px;top:167px">Wood</div>
    <div class="abs lbl" style="left:196px;top:167px">Delivery</div>
    <div class="abs field" style="left:23px;top:190px;width:150px">Pine</div>
    <div class="abs field" style="left:196px;top:190px;width:150px">11/23/2011
      <svg style="position:absolute;right:7px;top:7px" width="14" height="15" viewBox="0 0 14 15"><rect x="1" y="2.5" width="12" height="11" fill="none" stroke="#888" stroke-width="1.5"/><line x1="1" y1="6" x2="13" y2="6" stroke="#888" stroke-width="1.5"/><line x1="4" y1="0.5" x2="4" y2="4" stroke="#888" stroke-width="1.5"/><line x1="10" y1="0.5" x2="10" y2="4" stroke="#888" stroke-width="1.5"/></svg>
    </div>
    <div class="abs lbl" style="left:23px;top:252px">Quantity</div>
    <div class="abs lbl" style="left:196px;top:252px">Sets</div>
    <div class="abs field" style="left:23px;top:275px;width:150px">2</div>
    <div class="abs field" style="left:196px;top:275px;width:150px">1</div>
    <div class="abs btn">Search</div>
  </div>
  <div class="abs table">
    <div class="trow head"><span class="c1">COLLECTION</span><span class="c2">ITEM</span><span class="c3">WOOD</span><span class="c4">LEAD TIME</span><span class="c5">PRICE</span></div>
    <div class="trow"><span class="c1">Mountain</span><span class="c2">Log Bed Frame</span><span class="c3">Lodgepole Pine</span><span class="c4">12 days</span><span class="c5"><span class="old">1 099 €</span><b class="price">899 €</b></span></div>
    <div class="trow"><span class="c1">Country</span><span class="c2">Barnwood Dresser</span><span class="c3">Reclaimed Oak</span><span class="c4">10 days</span><span class="c5"><span class="old">1 099 €</span><b class="price">749 €</b></span></div>
    <div class="trow"><span class="c1">Mountain</span><span class="c2">Cabin Dining Table</span><span class="c3">Cedar</span><span class="c4">10 days</span><span class="c5"><span class="old">1 099 €</span><b class="price">799 €</b></span></div>
    <div class="trow"><span class="c1">Country</span><span class="c2">Ranch Bench</span><span class="c3">Reclaimed Pine</span><span class="c4">9 days</span><span class="c5"><span class="old">1 099 €</span><b class="price">799 €</b></span></div>
    <div class="trow"><span class="c1">Mountain</span><span class="c2">Lodge Armchair Set</span><span class="c3">Aspen</span><span class="c4">9 days</span><span class="c5"><span class="old">1 099 €</span><b class="price">749 €</b></span></div>
    <div class="trow"><span class="c1">Country</span><span class="c2">Barn Door Cabinet</span><span class="c3">Reclaimed Fir</span><span class="c4">9 days</span><span class="c5"><span class="old">1 099 €</span><b class="price">849 €</b></span></div>
    <div class="trow"><span class="c1">Mountain</span><span class="c2">Log Bed Frame</span><span class="c3">Lodgepole Pine</span><span class="c4">11 days</span><span class="c5"><span class="old">1 099 €</span><b class="price">899 €</b></span></div>
  </div>
</section>

<div class="abs dashes" style="top:1419px"></div>

<article class="abs post" style="left:40px">
  <div class="post-photo" role="img" aria-label="Carved coat rack with hooks on weathered barnwood" style="background:linear-gradient(180deg,#6d6a62 0%,#8a8780 40%,#5d5a52 70%,#4a463f 100%)"></div>
  <h2 class="post-title">Barnwood hooks</h2>
  <div class="post-meta"><span>by <b>Ada Mercer</b></span><span>8 comments</span><span>Nov 04</span></div>
  <p class="post-body">Old fence boards and barn siding get a second life as coat racks and wall hooks. Each board keeps its nail holes, saw marks and weathered grey patina, so no two racks are ever quite the same. Hang one by the door of any ranch house.</p>
</article>

<article class="abs post" style="left:422px">
  <div class="post-photo" role="img" aria-label="Rustic log table with lamps and décor against a brick wall" style="background:linear-gradient(180deg,#8a3d2a 0%,#a14c33 45%,#7a4a26 65%,#c98a4a 80%,#6d5440 100%)"></div>
  <h2 class="post-title">Live-edge log tables</h2>
  <div class="post-meta"><span>by <b>Ada Mercer</b></span><span>8 comments</span><span>Sep 16</span></div>
  <p class="post-body">Our live-edge tables start as single slabs of pine and cedar, dried slowly and sealed by hand. The natural edge keeps the shape of the tree, while a clear oil finish brings out the warm grain. Pair one with our log benches.</p>
</article>

<article class="abs post" style="left:804px">
  <div class="post-photo" role="img" aria-label="Pair of glowing table lamps with wooden bases" style="background:linear-gradient(180deg,#3a2418 0%,#c98a55 30%,#e8b884 45%,#7a5236 70%,#d9c8b4 100%)"></div>
  <h2 class="post-title">Lamps for the lodge</h2>
  <div class="post-meta"><span>by <b>Ada Mercer</b></span><span>8 comments</span><span>Aug 15</span></div>
  <p class="post-body">Turned from branch wood and topped with linen shades, these table lamps give a cabin a soft evening glow. Every base is sanded and waxed by hand, and each one ships wired and ready for the nightstand or the lodge mantel.</p>
</article>

<footer>
  <div class="abs footer-rule"></div>
  <nav class="abs foot-nav"><span>Home</span><span>Catalogue</span><span>Blog</span><span>Contact</span><span>FAQ</span></nav>
  <div class="abs copy">© 2011 Birch &amp; Ember</div>
  <address class="abs contact"><b>Birch &amp; Ember Supply House</b><br>48 Cedar Lane , Boulder<br>hello@birchandember.example</address>
</footer>

</body>
</html>
```